"Every Lantern Still Burning" Sermon Series Design

Needing a design for our church's next sermon series titled "Every Lantern Still Burning" where we will discuss the need for unity, diversity, love and clarity. Looking for a 1920 x 1080 (or higher res) editable and layered file (PSD or AI) so that we can reformat the design to work on social, screens, lower thirds and various print and online mediums. We will also need to have access to the font files so that we can make resize and tweak as needed. We like the idea of using a globe or map of the world as the backdrop with the words overtop. Or, the idea of creating a bunch of newspaper clippings (generic, so that they can't actually be read) and making the shape of a heart. See attached examples. This website will give you an idea of our previous sermon series designs so you can have an idea of our style (but, feel free to help us advance the ball on something more aligned with current design trends): https://www.brinmoorfellowship.church/series

Examples use red, but stay away from a ton of red. If you're gonna major in a color, use blue or something in that family.

Must haves:
Title: Every Lantern Still Burning
Tagline : (TBD - use some Lorem Ipsum as a placeholder and we will fill in later)
Our Logo (attached) (small towards bottom is standard - only use solid colors for logo - preferably just solid black or white)

Industry/Entity Type

Church

Font styles to use
Serif
Sans Serif

Requirements
Must have
• Title: Every Lantern Still Burning
Nice to have
• We like the idea of using a globe or map of the world as the backdrop with the words overtop. Or, the idea of creating a bunch of newspaper clippings (generic, so that they can't actually be read) and making the shape of a heart. See attached examples.

If you're gonna major on a color, stick with blue or something close.
Should not have
• Don't use red as the primary color (example we sent has red, but stay away from it)

```html
<!DOCTYPE html>
<html lang="en">
<head>
<meta charset="utf-8">
<title>Every Lantern Still Burning — Sermon Series</title>
<link rel="stylesheet" href="https://fonts.googleapis.com/css2?family=Forum&family=Raleway:wght@700&display=swap">
<style>
  :root {
    --page: #c9c7c8;
    --teal-deep: #0c5a6e;
    --teal-mid: #1c7d90;
    --teal-glow: #4aa5b2;
    --ink-white: #ffffff;
    --cross-solid: #8fd2f2;
    --cross-line: #a9def6;
    --globe-ocean: #2a4f8f;
    --globe-land: #4d8a5a;
    --scope-dark: #1d2a30;
  }
  * { margin: 0; padding: 0; box-sizing: border-box; }
  html, body {
    width: 1200px;
    height: 872px;
    overflow: hidden;
    background: var(--page);
  }
  .series-banner {
    position: absolute;
    left: 78px;
    top: 143px;
    width: 1045px;
    height: 586px;
    overflow: hidden;
    background:
      radial-gradient(ellipse 60% 70% at 55% 55%, var(--teal-glow) 0%, rgba(74,165,178,0) 70%),
      linear-gradient(160deg, var(--teal-mid) 0%, var(--teal-deep) 100%);
  }
  .banner-art {
    position: absolute;
    inset: 0;
    width: 1045px;
    height: 586px;
  }
  .series-title {
    position: absolute;
    left: 251px;
    top: 92px;
    width: 500px;
    text-align: center;
    font-family: "Forum", serif;
    color: var(--ink-white);
    font-weight: 400;
  }
  .series-title span { display: block; line-height: 0.98; }
  .title-line-small { font-size: 58px; }
  .title-line-large { font-size: 100px; }
  .title-line-end { font-size: 64px; margin-top: 2px; }
  .church-mark {
    position: absolute;
    left: 60px;
    top: 502px;
    display: flex;
    align-items: center;
    gap: 10px;
  }
  .church-mark-dot {
    width: 40px;
    height: 40px;
    border-radius: 50%;
    border: 3px solid var(--ink-white);
  }
  .church-mark-name {
    font-family: "Raleway", sans-serif;
    font-weight: 700;
    font-size: 15px;
    line-height: 1.2;
    color: var(--ink-white);
  }
  .series-tagline {
    position: absolute;
    left: 221px;
    top: 508px;
    width: 600px;
    text-align: center;
    font-family: "Raleway", sans-serif;
    font-weight: 700;
    font-size: 20px;
    line-height: 27px;
    color: var(--ink-white);
  }
</style>
</head>
<body>
  <main class="series-banner">
    <svg class="banner-art" viewBox="0 0 1045 586" xmlns="http://www.w3.org/2000/svg">
      <defs>
        <path id="plus" d="M1 0h1v1h1v1h-1v1h-1v-1h-1v-1h1z"/>
        <radialGradient id="globe-tones" cx="40%" cy="40%" r="70%">
          <stop offset="0%" stop-color="var(--globe-land)"/>
          <stop offset="55%" stop-color="var(--globe-ocean)"/>
          <stop offset="100%" stop-color="#1d3a6b"/>
        </radialGradient>
        <radialGradient id="scope-tones" cx="40%" cy="40%" r="65%">
          <stop offset="0%" stop-color="#4b5a60"/>
          <stop offset="100%" stop-color="var(--scope-dark)"/>
        </radialGradient>
      </defs>

      <path class="globe-heart" role="img" aria-label="Photo of planet Earth shaped as a heart"
            fill="url(#globe-tones)"
            d="M495 112 C455 40 330 22 285 110 C250 190 288 300 495 466 C702 300 740 190 705 110 C660 22 535 40 495 112Z"/>

      <circle class="stethoscope-chestpiece" role="img" aria-label="Photo of a stethoscope chest piece"
              cx="858" cy="443" r="49" fill="url(#scope-tones)"/>

      <g class="cross-outline" fill="none" stroke="var(--cross-line)">
        <use href="#plus" transform="translate(935 -35) scale(43)" stroke-width="0.05"/>
        <use href="#plus" transform="translate(820 75) scale(26.3)" stroke-width="0.07"/>
        <use href="#plus" transform="translate(981 103) scale(10)" stroke-width="0.18"/>
        <use href="#plus" transform="translate(1006 147) scale(14.7)" stroke-width="0.12"/>
        <use href="#plus" transform="translate(46 266) scale(18)" stroke-width="0.1"/>
      </g>
      <g class="cross-solid" fill="var(--cross-solid)">
        <use href="#plus" transform="translate(887 54) scale(16.7)"/>
        <use href="#plus" transform="translate(917 114) scale(13.3)"/>
        <use href="#plus" transform="translate(939 470) scale(28.7)"/>
      </g>
    </svg>

    <h1 class="series-title">
      <span class="title-line-small">Every</span>
      <span class="title-line-large">Lantern</span>
      <span class="title-line-large">Still</span>
      <span class="title-line-end">Burning</span>
    </h1>

    <div class="church-mark">
      <div class="church-mark-dot"></div>
      <p class="church-mark-name">Brinmoor<br>Fellowship</p>
    </div>

    <p class="series-tagline">Lorem Ipsum is simply dummy text of the printing<br>and typesetting industry.</p>
  </main>
</body>
</html>
```